Consumer Facing Energy Data Analytics Startup Needs a Postcard to Promote New Product

We need a set of 2 postcards (6 x 4.25 inches as describers in the attached files) to help us promote our product for a new company based in San Francisco called "Lumo Crest".
We develop an alert platform for customers of energy utility companies. Our initial product is "Lumo Notice" - an application that helps people better manage their energy bill by sending an SMS or email alter in advance of a high bill.
We would like to see designs that use the colors blue and orange (same as in the website: www.lumocrest-demo.com). The text of the postcards will be reworked once a layout has been chosen, but we welcome original ways to attract the customers' attention.
Our goal is ultimately to have our targets go the our website and sign up for our service.
The final deliverable should be 8 vector files (preferable .eps, 4 file types, one version in print and one in web format):
- front of card for our small and medium business customers
- front of card for our residential customers
- back of card for our small and medium business customers
- back of card for our residential customers
- DINPro and Avenir

```html
<!DOCTYPE html>
<html lang="en">
<head>
<meta charset="utf-8">
<title>Lumo Notice Postcard</title>
<link rel="stylesheet" href="https://fonts.googleapis.com/css2?family=Barlow:wght@400;500&family=Nunito+Sans:wght@600;700&display=swap">
<style>
  :root {
    --blue: #2ca7e0;
    --orange: #fbb040;
    --white: #ffffff;
    --ink: #1d1d1f;
    --card-light: #ffffff;
    --card-shade: #ececec;
  }
  html, body {
    margin: 0;
    padding: 0;
    width: 1200px;
    height: 918px;
    overflow: hidden;
    background: #e6e6e6;
  }
  .postcard {
    position: relative;
    width: 1200px;
    height: 918px;
    overflow: hidden;
    background: radial-gradient(ellipse at 40% 55%, var(--card-light) 0%, var(--card-light) 45%, var(--card-shade) 100%);
    font-family: "Nunito Sans", sans-serif;
  }
  .cloud-band {
    position: absolute;
    top: 0;
    left: 0;
    width: 1200px;
    height: 400px;
  }
  .tagline {
    position: absolute;
    top: 56px;
    left: 470px;
    margin: 0;
    font-family: "Barlow", sans-serif;
    font-weight: 400;
    font-size: 23px;
    color: var(--white);
    white-space: nowrap;
  }
  .about {
    position: absolute;
    top: 122px;
    left: 612px;
    width: 518px;
    margin: 0;
    font-family: "Barlow", sans-serif;
    font-weight: 400;
    font-size: 22px;
    line-height: 31px;
    text-align: justify;
    color: var(--white);
  }
  .brand-name {
    position: absolute;
    top: 268px;
    left: 56px;
    margin: 0;
    font-family: "Barlow", sans-serif;
    font-weight: 500;
    font-size: 42px;
    letter-spacing: 5px;
    color: var(--blue);
    white-space: nowrap;
  }
  .benefits {
    position: absolute;
    left: 44px;
    top: 353px;
    width: 586px;
    margin: 0;
    padding: 0;
    list-style: none;
  }
  .benefit {
    display: flex;
    align-items: center;
    justify-content: center;
    height: 112px;
    margin-bottom: 12px;
    border-radius: 56px;
    text-align: center;
    color: var(--white);
    font-weight: 600;
    font-size: 27px;
    line-height: 35px;
    padding: 0 24px;
    box-sizing: border-box;
  }
  .benefit--orange { background: var(--orange); }
  .benefit--blue { background: var(--blue); }
  .contact {
    position: absolute;
    top: 860px;
    left: 68px;
    display: flex;
    gap: 46px;
    font-weight: 700;
    font-size: 25px;
    color: var(--ink);
  }
  .contact-item {
    display: flex;
    align-items: center;
    gap: 6px;
  }
  .contact-item svg { width: 22px; height: 22px; }
  .hero-photo {
    position: absolute;
    left: 720px;
    top: 360px;
    width: 480px;
    height: 558px;
    background: linear-gradient(160deg, #f6f6f6 0%, #e9d8cc 35%, #c9a58d 55%, #eef0f2 75%, #7f9bbd 100%);
    border-top-left-radius: 240px;
  }
</style>
</head>
<body>
  <main class="postcard">
    <svg class="cloud-band" viewBox="0 0 1200 400" aria-hidden="true">
      <path fill="var(--blue)" d="M331,0 H1200 V330 C1160,300 1110,292 1080,318 C1030,362 900,372 840,358 C760,340 700,300 640,302 C560,304 470,262 440,200 C418,150 385,40 331,0 Z"/>
    </svg>

    <p class="tagline">Lumo Crest helps you predict and avoid your high energy bills.</p>
    <p class="about">Lumo Crest employs advanced analytics software to assess customer energy use on a daily basis. We predict monthly energy bills based on current usage, and provide customer alerts and tips when use is above normal.</p>

    <h1 class="brand-name">LUMO NOTICE</h1>

    <ul class="benefits">
      <li class="benefit benefit--orange">Never get the bad surprise of a high energy bill again with Lumo Notice.</li>
      <li class="benefit benefit--blue">Our email alerts will put you in control of your energy usage</li>
      <li class="benefit benefit--orange">Get your alerts on the go by email or SMS so you're always in control</li>
      <li class="benefit benefit--blue">Save on your energy expenses with our simple and easy timely recommendations</li>
    </ul>

    <div class="contact">
      <span class="contact-item">
        <svg viewBox="0 0 24 24" aria-hidden="true"><circle cx="12" cy="12" r="10.5" fill="none" stroke="var(--ink)" stroke-width="2"/><path d="M8.5 7 l2 2 -1 1.5 c0.8 1.8 2.2 3.2 4 4 l1.5 -1 2 2 -1.5 1.8 c-4 -0.5 -8 -4.5 -8.5 -8.5 z" fill="var(--ink)"/></svg>
        000-000-0000
      </span>
      <span class="contact-item">
        <svg viewBox="0 0 24 24" aria-hidden="true"><g fill="none" stroke="var(--ink)" stroke-width="2"><circle cx="12" cy="12" r="9"/><ellipse cx="12" cy="12" rx="4" ry="9"/><line x1="3" y1="12" x2="21" y2="12"/></g></svg>
        www.lumocrest-demo.com
      </span>
    </div>

    <div class="hero-photo" role="img" aria-label="Photo of a smiling woman sitting and typing on a laptop"></div>
  </main>
</body>
</html>
```